TWMP site redesign

Please redesign a home page with content provided. PSD only - no coding
Can use any images from pixelvault-sample.com

Please create a site design that more clearly illustrates the client's services and expertise. We are looking for a high-end design.

Any images used must be generic or of Dallas TX.

Fonts: Any
Colors: Match to logo
Look: Modern - Professional

Target Market(s)

medium-large business owners

Number of Pages Required

1 page

Font styles to use
Serif
Sans Serif

Requirements
Must have
• cohesive professional design
• high end look
• Match to logo

```html
<!DOCTYPE html>
<html lang="en">
<head>
<meta charset="utf-8">
<title>TWMP – Professional Office and Warehouse Leasing</title>
<link href="https://fonts.googleapis.com/css2?family=Tinos:ital,wght@0,400;0,700;1,700&family=Lato:wght@400;700&display=swap" rel="stylesheet">
<style>
:root{
  --red:#c4000b;
  --red-dark:#a30009;
  --ink:#1b1b1b;
  --grey-text:#6f6f6f;
  --card:#f1f1f1;
  --line:#d8d8d8;
  --white:#ffffff;
  --black:#0a0a0a;
}
*{box-sizing:border-box;margin:0;padding:0}
html,body{width:1200px;height:4401px;overflow:hidden}
body{position:relative;background:var(--white);font-family:"Lato",Arial,sans-serif;color:var(--ink)}
.abs{position:absolute}
.serif{font-family:"Tinos","Times New Roman",serif}
.photo{position:absolute}
.btn{position:absolute;display:flex;align-items:center;justify-content:center;background:var(--red);color:var(--white);font-size:17px;text-transform:uppercase;border:2px solid var(--white);outline:2px solid var(--red)}

/* hero */
.hero{left:0;top:0;width:1200px;height:680px;background:linear-gradient(90deg,#3b3b3b 0%,#707070 45%,#b9b4ae 65%,#5c5a58 100%)}
.hero-figure{left:640px;top:110px;width:360px;height:570px;background:linear-gradient(180deg,#8a6a55,#d9d2c8 45%,#c9c4bd)}
.logo{left:82px;top:22px;display:flex;align-items:center;gap:10px}
.logo-mark{width:22px;height:22px;background:var(--red)}
.logo-name{font-family:"Tinos",serif;font-weight:700;font-size:40px;color:var(--white)}
.nav{left:305px;top:46px;display:flex;gap:32px;font-size:16px;color:var(--white)}
.phone-pill{left:945px;top:38px;width:175px;height:42px;border-radius:21px;background:var(--white);display:flex;align-items:center;justify-content:center;gap:8px;font-size:16px;color:var(--ink)}
.hero-title{left:80px;top:210px;font-size:84px;font-weight:700;color:var(--white)}
.hero-sub{left:80px;top:312px;font-size:27px;font-weight:700;color:var(--white)}
.hero-text{left:80px;top:355px;width:540px;font-size:17px;line-height:22px;color:var(--white)}
.dots{left:560px;top:594px;display:flex;gap:10px}
.dots span{width:18px;height:18px;border-radius:50%;border:2px solid var(--white)}
.dots span.on{background:var(--white)}

/* why */
.why-title{left:80px;top:735px;font-size:36px;line-height:42px;font-weight:700;color:var(--red)}
.why-text{left:80px;top:850px;width:330px;font-size:14px;line-height:21px;color:var(--grey-text)}
.why-photo{left:80px;top:975px;width:330px;height:310px;background:linear-gradient(160deg,#9da1a3,#cfd0cd 60%,#7f8486)}
.card{position:absolute;width:335px;height:256px;background:var(--card);box-shadow:0 3px 8px rgba(0,0,0,.15);text-align:center;padding-top:40px}
.card h3{font-size:21px;font-weight:400;color:var(--red);margin:14px 0 10px}
.card p{font-size:13px;line-height:20px;color:var(--grey-text);padding:0 30px}
.card.accent{background:var(--red)}
.card.accent h3,.card.accent p{color:var(--white)}

/* banner */
.banner{left:0;top:1355px;width:1200px;height:355px;background:linear-gradient(180deg,#2e3230,#4b4c44 50%,#2a2b28)}
.banner-text{left:0;top:1415px;width:1200px;text-align:center;font-size:36px;line-height:44px;font-style:italic;font-weight:700;color:var(--white)}

/* team */
.sec-title{left:0;width:1200px;text-align:center;font-size:34px;font-weight:700;color:var(--red)}
.team-text{left:220px;top:1838px;width:760px;text-align:center;font-size:13px;line-height:23px;color:var(--grey-text)}
.team-rail{left:80px;top:1980px;width:185px;height:534px;background:var(--black)}
.team-rail-top{left:80px;top:1980px;width:185px;height:206px;background:var(--red)}
.avatar{position:absolute;border-radius:50%;border:4px solid var(--white);background:linear-gradient(180deg,#c9a58b,#8f6a57)}
.team-photo{left:265px;top:1980px;width:859px;height:450px;background:linear-gradient(180deg,#d7e3ec,#a9bccb 45%,#5d7a55 80%,#3f5a3b)}
.team-caption{left:265px;top:2430px;width:859px;height:84px;background:var(--card);text-align:center;padding-top:14px}
.team-caption small{display:block;font-size:13px;color:var(--ink)}
.team-caption strong{display:block;font-family:"Tinos",serif;font-size:25px;color:var(--red);margin-top:4px}

/* testimonials */
.testi{left:0;top:2582px;width:1200px;height:578px;background:linear-gradient(90deg,#1b1816,#3d322b 55%,#231f1c)}
.testi-title{left:0;top:2645px;width:1200px;text-align:center;font-size:34px;color:var(--white)}
.testi-box{left:185px;top:2758px;width:830px;height:229px;border:2px solid #bdbdbd}
.quote{left:567px;top:2740px;width:66px;height:54px;background:var(--white);display:flex;align-items:center;justify-content:center;font-family:"Tinos",serif;font-size:56px;font-weight:700;color:var(--red);line-height:1}
.testi-text{left:220px;top:2820px;width:760px;text-align:center;font-size:14.5px;line-height:27px;color:var(--white)}
.arrow{position:absolute;width:38px;height:38px;background:var(--white);display:flex;align-items:center;justify-content:center}
.testi-name{left:0;top:3066px;width:1200px;text-align:center;font-size:22px;font-weight:700;color:var(--white)}

/* blog */
.post-img{position:absolute;width:249px;height:164px}
.post{position:absolute;width:230px}
.post .date{display:flex;align-items:center;gap:8px;font-size:13px;color:var(--ink);padding-bottom:8px;border-bottom:1px solid var(--line)}
.post h4{font-family:"Tinos",serif;font-size:16px;line-height:20px;color:var(--red);margin:10px 0 6px}
.post p{font-size:13px;line-height:20px;color:var(--grey-text)}

/* appointment */
.appt{left:0;top:3556px;width:1200px;height:449px;background:linear-gradient(180deg,#f3f3f3,#cfd2d4)}
.news{left:80px;top:3618px;width:392px;height:308px;background:#2d2d2d;padding:30px 24px;color:var(--white)}
.news p{font-size:14px;line-height:22px}
.news-form{display:flex;margin-top:16px}
.news-form span{flex:1;height:62px;background:var(--white);color:#555;font-size:13px;display:flex;align-items:center;padding-left:12px}
.news-form b{width:106px;height:62px;background:var(--red);font-size:15px;display:flex;align-items:center;justify-content:center}
.news small{display:block;font-size:12px;margin-top:10px}
.social{display:flex;justify-content:center;gap:8px;margin-top:14px}
.social i{width:26px;height:26px;border-radius:50%;background:#3d7fc6}
.appt-title{left:563px;top:3612px;width:561px;text-align:center;font-size:36px;font-weight:700;color:var(--red)}
.field{position:absolute;width:267px;height:61px;background:var(--white);font-size:14px;color:#444;display:flex;align-items:center;justify-content:space-between;padding:0 14px}

/* footer */
.footer{left:0;top:4005px;width:1200px;height:396px;background:var(--black);color:var(--white)}
.f-head{position:absolute;top:4064px;font-family:"Tinos",serif;font-size:23px;font-weight:700;color:var(--red)}
.f-text{position:absolute;font-size:13.5px;line-height:24px;color:var(--white)}
.f-row{display:flex;gap:12px;align-items:flex-start;margin-bottom:12px}
</style>
</head>
<body>

<!-- Hero -->
<div class="photo hero" role="img" aria-label="Modern office lounge interior with city windows"></div>
<div class="photo hero-figure" role="img" aria-label="Smiling businesswoman pointing upward"></div>
<div class="abs logo"><span class="logo-mark"></span><span class="logo-name">TWMP</span></div>
<nav class="abs nav"><span>Home</span><span>About TWMP</span><span>Services</span><span>Market News</span><span>Blog</span><span>Contact Us</span></nav>
<div class="abs phone-pill">
  <svg width="16" height="16" viewBox="0 0 24 24"><path d="M6.6 10.8a15 15 0 006.6 6.6l2.2-2.2c.3-.3.7-.4 1-.2 1.1.4 2.3.6 3.6.6.6 0 1 .4 1 1V20c0 .6-.4 1-1 1A17 17 0 013 4c0-.6.4-1 1-1h3.5c.6 0 1 .4 1 1 0 1.3.2 2.5.6 3.6.1.3 0 .7-.2 1z" fill="#1b1b1b"/></svg>
  <span>555-014-2626</span>
</div>
<h1 class="abs serif hero-title">TWMP</h1>
<div class="abs serif hero-sub">Professional Office and Warehouse Leasing</div>
<p class="abs hero-text">Fast-track your search with tenant reps that only serve you, and specialize in the DFW area.</p>
<div class="btn" style="left:80px;top:440px;width:172px;height:58px">Contact Us</div>
<div class="abs dots"><span class="on"></span><span></span><span></span></div>

<!-- Why tenant representation -->
<h2 class="abs serif why-title">Why Tenant<br>Representation?</h2>
<p class="abs why-text">Lorem Ipsum is simply dummy text of the printing and typesetting industry. Lorem Ipsum has been the industry's standard dummy text ever since the 1500s.</p>
<div class="photo why-photo" role="img" aria-label="Business people shaking hands outdoors"></div>

<div class="card" style="left:434px;top:740px">
  <svg width="64" height="46" viewBox="0 0 64 46"><path d="M4 18l14-12 10 6 8-4 10 4 14 10-18 18-10-8-10 8z" fill="#1b1b1b"/></svg>
  <h3>Relationships</h3>
  <p>Save time by trusting TWMP year after year to find the right location for you. Once we've worked together...[+]</p>
</div>
<div class="card" style="left:789px;top:740px">
  <svg width="50" height="50" viewBox="0 0 50 50"><circle cx="22" cy="14" r="10" fill="#1b1b1b"/><path d="M4 46c0-12 8-20 18-20s18 8 18 20z" fill="#1b1b1b"/><circle cx="38" cy="36" r="8" fill="#1b1b1b" stroke="#f1f1f1" stroke-width="3"/></svg>
  <h3>Access to More</h3>
  <p>We have no agreements or personal incentives for specific properties, so we can always show you the offices...[+]</p>
</div>
<div class="card" style="left:434px;top:1024px">
  <svg width="60" height="50" viewBox="0 0 60 50"><rect x="10" y="4" width="46" height="36" fill="none" stroke="#1b1b1b" stroke-width="4"/><rect x="2" y="12" width="46" height="36" fill="#1b1b1b"/><path d="M8 42l12-14 8 8 6-6 10 12z" fill="#f1f1f1"/></svg>
  <h3>Free To You</h3>
  <p>You pay us nothing. We get our commission from the property being leased.</p>
</div>
<div class="card accent" style="left:789px;top:1024px">
  <svg width="56" height="50" viewBox="0 0 56 50"><circle cx="28" cy="12" r="9" fill="#fff"/><path d="M4 34h12l10 6h12c3 0 3 4 0 4H24M4 34v14h40l10-12c2-3-2-5-4-3l-8 7" fill="none" stroke="#fff" stroke-width="4"/></svg>
  <h3>Customized Service</h3>
  <p>Aside from saving you the time of repeating what your needs are to each new location, we also provide...[+]</p>
</div>

<!-- Banner -->
<div class="photo banner" role="img" aria-label="Aerial view of Dallas Fort Worth neighborhood"></div>
<p class="abs serif banner-text">If you need to find office or warehouse space in the<br>Dallas Fort Worth area, the team at TWMP has the<br>experience you need.</p>
<div class="btn" style="left:488px;top:1578px;width:224px;height:60px">Space Calculator</div>

<!-- Meet the team -->
<h2 class="abs serif sec-title" style="top:1770px">Meet the Team</h2>
<p class="abs team-text">At TWMP we believe that you deserve the best professional advice and personal service with your commercial real estate negotiations. By choosing TWMP as your tenant reps in the Dallas/Fort Worth area, you will receive the assistance of accomplished and experienced commercial real estate brokers and salespeople who are licensed by the State Realty Licensing Board to practice in Texas since 1982.</p>
<div class="abs team-rail"></div>
<div class="abs team-rail-top"></div>
<svg class="abs" style="left:265px;top:2050px" width="28" height="56" viewBox="0 0 28 56"><path d="M0 0l28 28L0 56z" fill="#c4000b"/></svg>
<div class="avatar" role="img" aria-label="Team member portrait" style="left:116px;top:2010px;width:112px;height:112px"></div>
<div class="avatar" role="img" aria-label="Team member portrait" style="left:116px;top:2204px;width:112px;height:112px"></div>
<div class="avatar" role="img" aria-label="Team member portrait" style="left:116px;top:2366px;width:112px;height:112px"></div>
<div class="photo team-photo" role="img" aria-label="Modern glass office building with trees"></div>
<div class="abs team-caption"><small>Commercial Property Specialist</small><strong>Dean Caldwell-Ross</strong></div>

<!-- Testimonials -->
<div class="photo testi" role="img" aria-label="Couple reviewing documents at home"></div>
<h2 class="abs serif testi-title">Client Testimonials</h2>
<div class="abs testi-box"></div>
<div class="abs quote">“</div>
<p class="abs testi-text">The real estate team at TWMP has decades of experience in Commercial. One advantage of TWMP is they know all the properties that are about to become available, BEFORE they are available. They have the inside track on properties and they watch your back at the negotiating table. Very impressive with a polished approach. Let the team run with your next project and you won't be disappointed.</p>
<div class="arrow" style="left:166px;top:2854px"><svg width="12" height="16" viewBox="0 0 12 16"><path d="M10 2L3 8l7 6" fill="none" stroke="#c4000b" stroke-width="3"/></svg></div>
<div class="arrow" style="left:996px;top:2854px"><svg width="12" height="16" viewBox="0 0 12 16"><path d="M2 2l7 6-7 6" fill="none" stroke="#c4000b" stroke-width="3"/></svg></div>
<div class="avatar" role="img" aria-label="Client portrait" style="left:456px;top:2950px;width:80px;height:80px;background:#e2d8d0"></div>
<div class="avatar" role="img" aria-label="Client portrait" style="left:553px;top:2940px;width:94px;height:94px;background:#d8dde2"></div>
<div class="avatar" role="img" aria-label="Client portrait" style="left:664px;top:2950px;width:80px;height:80px;background:#d9dde6"></div>
<div class="abs serif testi-name">- Nathan Reid Colby</div>

<!-- Blog -->
<h2 class="abs serif sec-title" style="top:3220px">Recent Blog Posts</h2>
<div class="post-img" role="img" aria-label="Business meeting with documents" style="left:80px;top:3307px;background:linear-gradient(135deg,#dfe4ea,#8c99a8)"></div>
<div class="post" style="left:352px;top:3305px">
  <div class="date"><svg width="16" height="16" viewBox="0 0 16 16"><rect x="1" y="3" width="14" height="12" fill="none" stroke="#1b1b1b" stroke-width="2"/><path d="M1 7h14M5 1v4M11 1v4" stroke="#1b1b1b" stroke-width="2"/></svg>07 MAY 2018</div>
  <h4>Lorem Ipsum dummy text typesetting industry.</h4>
  <p>Lorem Ipsum is simply dummy text of the printing and text typesetting industry.</p>
</div>
<div class="post-img" role="img" aria-label="Agents showing an empty office space" style="left:622px;top:3307px;background:linear-gradient(135deg,#e8e2d8,#9a7b60)"></div>
<div class="post" style="left:894px;top:3305px">
  <div class="date"><svg width="16" height="16" viewBox="0 0 16 16"><rect x="1" y="3" width="14" height="12" fill="none" stroke="#1b1b1b" stroke-width="2"/><path d="M1 7h14M5 1v4M11 1v4" stroke="#1b1b1b" stroke-width="2"/></svg>07 MAY 2018</div>
  <h4>Lorem Ipsum dummy text typesetting industry.</h4>
  <p>Lorem Ipsum is simply dummy text of the printing and text typesetting industry.</p>
</div>

<!-- Appointment -->
<div class="photo appt" role="img" aria-label="Faded Dallas city skyline"></div>
<div class="abs news">
  <p>Sign up us today we will send you latest news, usefull tips at your mail address.</p>
  <div class="news-form"><span>Enter Email id...</span><b>SUBMIT</b></div>
  <small>* Your email id is very confidential</small>
  <div class="social"><i style="background:#3b5998"></i><i style="background:#2aa3ef"></i><i style="background:#0e76a8"></i><i style="background:#d9261c"></i></div>
</div>
<h2 class="abs serif appt-title">Make An Appointment</h2>
<div class="field" style="left:563px;top:3697px">Name :</div>
<div class="field" style="left:857px;top:3697px">Phone :</div>
<div class="field" style="left:563px;top:3785px">Email :</div>
<div class="field" style="left:857px;top:3785px">Select a Subject :<svg width="14" height="10" viewBox="0 0 14 10"><path d="M0 0h14L7 10z" fill="#c4000b"/></svg></div>
<div class="btn" style="left:565px;top:3866px;width:177px;height:58px">Send Request</div>

<!-- Footer -->
<div class="abs footer"></div>
<div class="f-head" style="left:80px">About Us</div>
<div class="f-text" style="left:80px;top:4112px;width:250px">Lorem Ipsum is simply dummy text of the printing and typesetting industry. Lorem Ipsum has been the industry's<br><u>READ MORE</u></div>
<div class="f-head" style="left:396px">Navigation</div>
<div class="f-text" style="left:396px;top:4118px;line-height:25px">Home<br>About Us<br>Our Services<br>Market News<br>Blog<br>Contact</div>
<div class="f-head" style="left:607px">Get In Touch</div>
<div class="f-text" style="left:607px;top:4114px;width:250px">
  <div class="f-row"><svg width="14" height="18" viewBox="0 0 14 18"><path d="M7 0a7 7 0 017 7c0 5-7 11-7 11S0 12 0 7a7 7 0 017-7z" fill="#c4000b"/><circle cx="7" cy="7" r="2.5" fill="#000"/></svg><span>1200 Elm Park Avenue @ Cedar Plaza Suite 410 Dallas, Texas 75201</span></div>
  <div class="f-row"><svg width="16" height="16" viewBox="0 0 24 24"><path d="M6.6 10.8a15 15 0 006.6 6.6l2.2-2.2c.3-.3.7-.4 1-.2 1.1.4 2.3.6 3.6.6.6 0 1 .4 1 1V20c0 .6-.4 1-1 1A17 17 0 013 4c0-.6.4-1 1-1h3.5c.6 0 1 .4 1 1 0 1.3.2 2.5.6 3.6.1.3 0 .7-.2 1z" fill="#c4000b"/></svg><span>555-014-2626</span></div>
  <div class="f-row"><svg width="16" height="16" viewBox="0 0 16 16"><rect x="1" y="1" width="14" height="14" fill="#c4000b"/><rect x="4" y="4" width="8" height="5" fill="#000"/></svg><span>555-014-3299</span></div>
  <div class="f-row"><svg width="16" height="14" viewBox="0 0 16 14"><rect x="0" y="1" width="16" height="12" fill="#c4000b"/><path d="M0 1l8 6 8-6" fill="none" stroke="#000" stroke-width="1.5"/></svg><span>info@twmpharlow.example</span></div>
</div>
<div class="f-text" style="left:901px;top:4060px;width:200px">© Copyright by<br>TWMP Commercial GROUP 2018.<br>All rights reserved.</div>

</body>
</html>
```